Art Deco Wedding Invitation

We need a wedding invitation designed for a 1920's Art Deco theme.
The wedding will take place in Berlin, which had a glamorous, modern and wild culture in the 1920's. This may offer some design inspiration.
The couple's names are Rowland and Liora and the wedding will take place on May 8, 2015.

Industry/Entity Type

Wedding

```html
<!DOCTYPE html>
<html lang="en">
<head>
<meta charset="utf-8">
<title>Rowland &amp; Liora – 1920's Wedding Invitation</title>
<link rel="stylesheet" href="https://fonts.googleapis.com/css2?family=Pinyon+Script&family=Cormorant+Garamond:ital,wght@1,500;1,600&display=swap">
<style>
  :root {
    --navy: #262d4d;
    --silver: #d0d0d3;
    --white: #ffffff;
    --ink: #111111;
    --script: "Pinyon Script", cursive;
    --serif: "Cormorant Garamond", serif;
  }
  * { margin: 0; padding: 0; box-sizing: border-box; }
  html, body { width: 1200px; height: 907px; overflow: hidden; background: var(--white); }
  .card { position: relative; width: 1200px; height: 907px; }

  /* Outside cover */
  .cover { position: absolute; left: 0; top: 0; width: 590px; height: 907px; background: var(--white); }
  .label { position: absolute; left: 80px; top: 298px; width: 428px; height: 175px; background: var(--navy); overflow: hidden; }
  .label-ornament { position: absolute; top: 0; height: 175px; width: 100px; background: var(--silver); }
  .label-ornament.left { left: 0; border-radius: 0 60% 60% 0 / 0 50% 50% 0; }
  .label-ornament.right { right: 0; border-radius: 60% 0 0 60% / 50% 0 0 50%; }
  .label-lines { position: absolute; left: 0; top: 0; }
  .label-title { position: absolute; left: 0; width: 100%; top: 8px; text-align: center; font-family: var(--script); font-size: 52px; color: var(--white); }
  .label-year { position: absolute; left: 0; width: 100%; top: 80px; text-align: center; font-family: var(--script); font-size: 28px; color: var(--silver); }
  .addressee { position: absolute; left: 158px; top: 522px; font-family: var(--script); font-size: 36px; color: var(--ink); display: flex; align-items: flex-end; }
  .addressee-line { display: inline-block; width: 228px; border-bottom: 1.5px solid var(--ink); margin-left: 4px; margin-bottom: 10px; }

  /* Inside invitation */
  .invite { position: absolute; left: 590px; top: 0; width: 610px; height: 907px; background: var(--navy); overflow: hidden; }
  .frame { position: absolute; left: 0; top: 0; }
  .corner-ornament { position: absolute; background: var(--silver); }
  .corner-ornament.top { left: 440px; top: 56px; width: 128px; height: 128px; border-radius: 0 0 0 70%; }
  .corner-ornament.bottom { left: 450px; top: 718px; width: 118px; height: 128px; border-radius: 70% 0 0 0; }
  .bride { position: absolute; left: 4px; top: 258px; width: 214px; height: 538px; border-radius: 90px 90px 30px 60px; background: linear-gradient(180deg, #f4f4f6 0%, #ffffff 60%, #e9e9ec 100%); }

  .verse, .details { position: absolute; left: 180px; width: 280px; text-align: center; font-family: var(--serif); font-style: italic; font-weight: 500; color: var(--white); }
  .verse { top: 142px; font-size: 28px; line-height: 37px; }
  .year { position: absolute; left: 250px; top: 262px; font-family: var(--script); font-size: 46px; color: var(--white); }
  .guest-line { position: absolute; left: 232px; top: 318px; font-family: var(--serif); font-style: italic; font-weight: 500; font-size: 21px; color: var(--white); }
  .rule { position: absolute; left: 230px; width: 222px; height: 3px; background: var(--silver); }
  .rule.upper { top: 368px; }
  .rule.lower { top: 534px; }
  .couple { position: absolute; left: 230px; width: 222px; top: 378px; text-align: center; font-family: var(--script); font-size: 54px; line-height: 52px; color: var(--white); }
  .details { left: 230px; width: 222px; top: 552px; font-size: 29px; line-height: 37px; }
</style>
</head>
<body>
<main class="card">
  <section class="cover">
    <div class="label">
      <div class="label-ornament left" role="img" aria-label="Art Deco fan ornament with navy daisies"></div>
      <div class="label-ornament right" role="img" aria-label="Art Deco fan ornament with navy daisies"></div>
      <svg class="label-lines" width="428" height="175" aria-hidden="true">
        <g stroke="#d0d0d3" stroke-width="4" fill="none">
          <line x1="100" y1="116" x2="330" y2="116"/>
          <line x1="86" y1="134" x2="342" y2="134"/>
          <line x1="70" y1="150" x2="358" y2="150"/>
        </g>
      </svg>
      <h1 class="label-title">Invitation</h1>
      <p class="label-year">1920's</p>
    </div>
    <p class="addressee">To:<span class="addressee-line"></span></p>
  </section>

  <section class="invite">
    <svg class="frame" width="610" height="907" aria-hidden="true">
      <g fill="#d0d0d3">
        <rect x="114" y="56" width="18" height="18"/>
        <rect x="114" y="822" width="18" height="18"/>
      </g>
      <g stroke="#d0d0d3" stroke-width="4" fill="none">
        <polyline points="134,300 134,72 170,72 170,58 442,58"/>
        <polyline points="146,300 146,84 158,84 158,70 442,70"/>
        <polyline points="158,300 158,96 440,96"/>
        <polyline points="540,186 540,720"/>
        <polyline points="552,186 552,720"/>
        <polyline points="564,186 564,720"/>
        <polyline points="140,790 140,812 450,812"/>
        <polyline points="152,790 152,824 450,824"/>
        <polyline points="164,790 164,836 450,836"/>
      </g>
    </svg>
    <div class="corner-ornament top" role="img" aria-label="Art Deco corner ornament with navy daisies"></div>
    <div class="corner-ornament bottom" role="img" aria-label="Art Deco corner ornament with navy daisies"></div>
    <div class="bride" role="img" aria-label="Silhouette illustration of a 1920's bride in a white gown and veil holding a bouquet, seen from behind"></div>

    <p class="verse">Friends, let’s go back<br>the time, glamorous,<br>modern and wild ...</p>
    <p class="year">1920's</p>
    <p class="guest-line">Please be our guest as we,</p>
    <div class="rule upper"></div>
    <h2 class="couple">Rowland<br>and<br>Liora</h2>
    <div class="rule lower"></div>
    <p class="details">join together<br>on May 8, 2015.<br>Linden Chapel<br>Aster Road<br>Berlin, Germany</p>
  </section>
</main>
</body>
</html>
```